Velmora Partners - website for real estate investment company

Create a bold, modern website that reflects Velmora’s success, professionalism, and credibility.
The design must stand out while maintaining a polished, corporate tone. (bold, but understated)
The client just created a new logo, and the website design must be in sync with the logo design. Information about the logo colors, fonts, and message are in the attached design brief.
Updates

Target Market(s)

b2b: banks, brokers, institutional partners, vendors, and property sellers.

Industry/Entity Type

real estate investment company

Number of Pages Required

1 page

Font styles to use
Sans Serif

Colors

Designer to choose colors to be used in the design.

Requirements
Must have
• 1. homepage design (psd) 2. a top banner image (psd) for a default inner page
Nice to have
• please see attached design brief
Should not have

```html
<!DOCTYPE html>
<html lang="en">
<head>
<meta charset="utf-8">
<title>Velmora Partners</title>
<link rel="stylesheet" href="https://fonts.googleapis.com/css2?family=Barlow:wght@400;500;600;700&family=Roboto:wght@400;500;700&display=swap">
<style>
:root{
  --red:#e31e24;
  --ink:#333333;
  --dark:#4a4a4a;
  --grey:#f0f0f0;
  --mid:#8a8a8a;
  --line:#cfcfcf;
  --white:#ffffff;
  --ghost:#ececec;
}
*{box-sizing:border-box;margin:0;padding:0}
html,body{width:1200px;height:3859px;overflow:hidden;background:var(--white)}
body{position:relative;font-family:"Roboto",Arial,sans-serif;color:var(--ink)}
.abs{position:absolute}
.display{font-family:"Barlow",Arial,sans-serif}

/* header */
.site-header{position:absolute;left:0;top:0;width:1200px;height:75px;background:var(--white)}
.brand{position:absolute;font-family:"Barlow",Arial,sans-serif;font-weight:700;color:var(--dark);letter-spacing:1px}
.brand--header{left:123px;top:10px;font-size:46px;line-height:55px}
.main-nav a{position:absolute;top:27px;font-family:"Barlow",Arial,sans-serif;font-weight:600;font-size:12.5px;color:var(--ink);text-decoration:none;letter-spacing:.3px}
.main-nav a.is-active::before{content:"";position:absolute;left:-8px;top:-6px;border-top:8px solid var(--red);border-right:8px solid transparent}
.btn-contact{position:absolute;left:1020px;top:19px;width:111px;height:32px;background:var(--red);color:var(--white);font:700 12.5px/32px "Barlow",Arial,sans-serif;text-align:center;text-decoration:none}

/* hero */
.hero{position:absolute;left:0;top:75px;width:1200px;height:595px;background:linear-gradient(180deg,#8d8d8d 0%,#6b6b6b 45%,#4e4e4e 70%,#5f5f5f 100%)}
.hero__title{position:absolute;left:0;width:1200px;top:303px;text-align:center;color:var(--white);font:700 56px/64px "Barlow",Arial,sans-serif;letter-spacing:1px}
.hero__rule{position:absolute;left:540px;top:376px;width:120px;height:3px;background:var(--white)}
.hero__text{position:absolute;left:220px;width:760px;top:408px;text-align:center;color:var(--white);font:400 22px/28px "Barlow",Arial,sans-serif}
.hero__play{position:absolute;left:1069px;top:510px}

/* stats */
.stats{position:absolute;left:0;top:670px;width:1200px;height:130px;background:var(--grey)}
.stat__num{position:absolute;font:500 35px/40px "Barlow",Arial,sans-serif;color:var(--ink)}
.stat__label{position:absolute;font:500 15px/19px "Barlow",Arial,sans-serif;color:var(--ink);letter-spacing:.4px}
.stat__divider{position:absolute;top:20px;width:1px;height:80px;background:var(--line)}

/* section headings */
.section-title{position:absolute;left:0;width:1200px;text-align:center;font:700 40px/46px "Barlow",Arial,sans-serif;color:var(--ink);letter-spacing:.5px}
.rule{position:absolute;height:3px;background:var(--ink)}
.ghost{position:absolute;font:700 76px/80px "Barlow",Arial,sans-serif;color:var(--ghost);letter-spacing:2px}

/* portfolio */
.project{position:absolute;top:914px;height:386px}
.project__bar{position:absolute;left:0;bottom:0;width:100%;height:61px;background:rgba(40,40,40,.72)}
.project__name{position:absolute;left:24px;top:16px;color:var(--white);font:700 22px/28px "Barlow",Arial,sans-serif;letter-spacing:1.5px}
.project__arrow{position:absolute;right:24px;top:20px}

/* buttons */
.btn{position:absolute;display:block;background:var(--ink);color:var(--white);font:700 15px/45px "Barlow",Arial,sans-serif;text-align:center;text-decoration:none;letter-spacing:.3px}
.btn::before{content:"";position:absolute;left:0;top:0;border-top:22px solid var(--red);border-right:22px solid transparent}
.btn--outline{background:transparent;border:1.5px solid var(--white);line-height:42px}

/* story */
.body-copy{position:absolute;font:400 18px/25px "Roboto",Arial,sans-serif;color:var(--ink)}
.h2{position:absolute;font:700 40px/46px "Barlow",Arial,sans-serif;color:var(--ink);letter-spacing:.5px}

/* testimonial */
.quote{position:absolute;left:427px;top:2530px;width:680px;font:400 22px/29px "Roboto",Arial,sans-serif;color:var(--ink)}
.quote__name{position:absolute;left:430px;top:2658px;font:500 21px/26px "Roboto",Arial,sans-serif}
.quote__role{position:absolute;left:427px;top:2693px;font:400 15px/20px "Roboto",Arial,sans-serif}

/* why us */
.why{position:absolute;left:0;top:2816px;width:1200px;height:640px;background:var(--dark);overflow:hidden}

/* footer */
.footer-contact{position:absolute;left:491px;font:400 18px/24px "Barlow",Arial,sans-serif;color:var(--ink)}
.footer-label{position:absolute;font:600 17px/22px "Barlow",Arial,sans-serif;color:var(--ink);letter-spacing:.5px}
.field{position:absolute;border:1px solid var(--line);background:var(--white);font:500 11px/14px "Roboto",Arial,sans-serif;color:var(--ink);padding:8px 16px}
.btn-send{position:absolute;left:779px;top:3664px;width:153px;height:37px;background:var(--red);color:var(--white);font:700 13px/37px "Barlow",Arial,sans-serif;text-align:center}
.btn-mail{position:absolute;left:460px;top:3667px;width:148px;height:36px;background:var(--dark);color:var(--white);font:700 12px/36px "Barlow",Arial,sans-serif;text-align:center}
.copyright{position:absolute;left:0;top:3790px;width:1200px;height:69px;background:var(--grey);text-align:center;font:400 15px/69px "Barlow",Arial,sans-serif;color:var(--ink)}
</style>
</head>
<body>

<header class="site-header">
  <div class="brand brand--header">VELMORA</div>
  <nav class="main-nav">
    <a class="is-active" style="left:366px" href="#">HOME</a>
    <a style="left:437px" href="#">OUR STORY</a>
    <a style="left:542px" href="#">INVESTMENT STRATEGY</a>
    <a style="left:725px" href="#">WHAT SETS US APART</a>
    <a style="left:893px" href="#">OUR PORTFOLIO</a>
  </nav>
  <a class="btn-contact" href="#">CONTACT &rsaquo;</a>
</header>

<section class="hero" role="img" aria-label="Black and white city skyline with a suspension bridge over the river">
  <h1 class="hero__title">EXPERIENCE – STRATEGY – VISION</h1>
  <div class="hero__rule"></div>
  <p class="hero__text">Velmora Partners is a vertically integrated real estate investment firm with a proven four-decade track record. We acquire, reposition, and operate high-performing assets across multiple sectors — always with a focus on exceptional, risk-adjusted returns.</p>
  <svg class="hero__play" width="52" height="52" viewBox="0 0 52 52" aria-hidden="true"><circle cx="26" cy="26" r="24" fill="none" stroke="#fff" stroke-width="3"/><path d="M21 16 L36 26 L21 36Z" fill="#fff"/></svg>
</section>

<section class="stats">
  <svg class="abs" style="left:164px;top:24px" width="34" height="34" viewBox="0 0 34 34" aria-hidden="true"><rect x="2" y="5" width="30" height="27" fill="none" stroke="#555" stroke-width="1.6"/><line x1="2" y1="12" x2="32" y2="12" stroke="#555" stroke-width="1.6"/><line x1="10" y1="1" x2="10" y2="8" stroke="#555" stroke-width="1.6"/><line x1="24" y1="1" x2="24" y2="8" stroke="#555" stroke-width="1.6"/><text x="17" y="25" font-size="8" text-anchor="middle" fill="#555" font-family="Barlow,Arial,sans-serif">1989</text></svg>
  <div class="stat__num" style="left:214px;top:16px">1989</div>
  <div class="stat__label" style="left:218px;top:60px">FOUNDED</div>
  <div class="stat__divider" style="left:379px"></div>

  <svg class="abs" style="left:450px;top:24px" width="38" height="32" viewBox="0 0 38 32" aria-hidden="true"><path d="M2 30 H36 M5 30 V10 L12 4 L19 10 L26 4 L33 10 V30" fill="none" stroke="#555" stroke-width="1.6"/><rect x="9" y="14" width="5" height="5" fill="none" stroke="#555" stroke-width="1.4"/><rect x="23" y="14" width="5" height="5" fill="none" stroke="#555" stroke-width="1.4"/><rect x="16" y="21" width="6" height="9" fill="none" stroke="#555" stroke-width="1.4"/></svg>
  <div class="stat__num" style="left:514px;top:16px">23,000+</div>
  <div class="stat__label" style="left:514px;top:60px">MULTIFAMILY &amp;<br>HEALTHCARE UNITS</div>
  <div class="stat__divider" style="left:760px"></div>

  <svg class="abs" style="left:814px;top:24px" width="42" height="42" viewBox="0 0 42 42" aria-hidden="true"><path d="M6 16 A17 17 0 0 1 36 12" fill="none" stroke="#555" stroke-width="1.6"/><path d="M36 26 A17 17 0 0 1 6 30" fill="none" stroke="#555" stroke-width="1.6"/><path d="M13 22 L21 15 L29 22 V30 H13Z" fill="none" stroke="#555" stroke-width="1.6"/><rect x="19" y="24" width="4" height="6" fill="#555"/></svg>
  <div class="stat__num" style="left:879px;top:19px">$300+</div>
  <div class="stat__label" style="left:879px;top:60px">MILLION INVESTED<br>IN RENOVATIONS</div>
</section>

<h2 class="section-title" style="top:840px">OUR PORTFOLIO</h2>
<div class="rule" style="left:569px;top:890px;width:66px"></div>

<article class="project" style="left:0;width:398px;background:linear-gradient(160deg,#2f6fb8 0%,#9fc2e2 45%,#d9d9d2 75%,#6d7f5a 100%)" role="img" aria-label="High-rise residential tower with palm trees under a blue sky">
  <div class="project__bar"><span class="project__name">PROJECT HEADING</span>
  <svg class="project__arrow" width="18" height="18" viewBox="0 0 18 18" aria-hidden="true"><path d="M2 16 L16 2 M6 2 H16 V12" fill="none" stroke="#fff" stroke-width="1.6"/></svg></div>
</article>
<article class="project" style="left:404px;width:399px;background:linear-gradient(180deg,#4c8fce 0%,#c9dbe9 40%,#6f7f88 70%,#3f5a4a 100%)" role="img" aria-label="Downtown skyscrapers and glass towers under a bright sky">
  <div class="project__bar"><span class="project__name">PROJECT HEADING</span>
  <svg class="project__arrow" width="18" height="18" viewBox="0 0 18 18" aria-hidden="true"><path d="M2 16 L16 2 M6 2 H16 V12" fill="none" stroke="#fff" stroke-width="1.6"/></svg></div>
</article>
<article class="project" style="left:809px;width:391px;background:linear-gradient(135deg,#5a3a2a 0%,#8a5b3e 35%,#3f86c9 60%,#1e9be0 100%)" role="img" aria-label="Modern apartment building with glass balconies against a blue sky">
  <div class="project__bar"><span class="project__name">PROJECT HEADING</span>
  <svg class="project__arrow" width="18" height="18" viewBox="0 0 18 18" aria-hidden="true"><path d="M2 16 L16 2 M6 2 H16 V12" fill="none" stroke="#fff" stroke-width="1.6"/></svg></div>
</article>

<section class="story">
  <svg class="abs" style="left:0;top:1360px" width="600" height="470" aria-hidden="true">
    <polygon points="0,0 40,0 40,340 0,420" fill="#f0f0f0"/>
    <polygon points="75,0 230,0 230,8 90,8 90,40 75,60" fill="#f0f0f0"/>
    <polygon points="91,15 340,15 115,220 115,240 91,265" fill="#e31e24"/>
    <rect x="103" y="26" width="483" height="434" fill="#fff" stroke="#c8c8c8" stroke-width="3"/>
  </svg>
  <div class="abs" style="left:115px;top:1398px;width:459px;height:410px;background:linear-gradient(135deg,#3a3a3a 0%,#7a7a7a 40%,#d9d9d9 75%,#a8a8a8 100%)" role="img" aria-label="Business people reviewing small architectural models of houses and buildings"></div>
  <div class="ghost" style="left:656px;top:1386px;font-size:72px">ABOUT US</div>
  <h2 class="h2" style="left:656px;top:1436px">OUR STORY</h2>
  <div class="rule" style="left:656px;top:1487px;width:74px"></div>
  <p class="body-copy" style="left:657px;top:1513px;width:470px">Lorem ipsum dolor sit amet, consectetur adipiscing elit, sed do eiusmod tempor incididunt ut labore et dolore</p>
  <p class="body-copy" style="left:657px;top:1590px;width:470px">Aagna aliqua. Quis ipsum suspendisse ultrices gravida. Risus commodo viverra maecenas accumsan lacus vel facilisis. Lorem ipsum dolor sit amet, consectetur adipiscing elit, sed do eiusmod tempor incididunt ut labore</p>
  <a class="btn" style="left:659px;top:1723px;width:162px;height:45px" href="#">LEARN MORE &rsaquo;</a>
</section>

<section class="abs" style="left:0;top:1902px;width:1200px;height:534px;background:linear-gradient(90deg,#dcdcdc 0%,#f4f4f4 40%,#f6f6f6 60%,#d6d6d6 100%)" role="img" aria-label="Faded upward view of tall office towers"></section>
<div class="ghost" style="left:0;width:1200px;text-align:center;top:1960px;color:rgba(200,200,200,.45)">INVESTMENT</div>
<h2 class="section-title" style="top:2016px">INVESTMENT STRATEGY</h2>
<div class="rule" style="left:567px;top:2071px;width:68px"></div>
<p class="body-copy" style="left:210px;width:780px;top:2095px;text-align:center">Lorem ipsum dolor sit amet, consectetur adipiscing elit, sed do eiusmod tempor incididunt ut labore et dolore&nbsp; Quis ipsum suspendisse ultrices gravida.</p>
<p class="body-copy" style="left:210px;width:780px;top:2173px;text-align:center">Risus commodo viverra maecenas accumsan lacus vel facilisis. Lorem ipsum dolor sit amet, consectetur adipiscing elit, sed do eiusmod tempor incididunt ut labore Lorem ipsum dolor sit amet, consectetur adipiscing elit sed.</p>
<a class="btn" style="left:521px;top:2287px;width:177px;height:45px" href="#">LEARN MORE &rsaquo;</a>

<section class="testimonial">
  <svg class="abs" style="left:120px;top:2496px" width="236" height="236" aria-hidden="true">
    <path d="M118 4 A114 114 0 0 0 45 205" fill="none" stroke="#e31e24" stroke-width="8"/>
    <path d="M118 4 A114 114 0 0 1 215 60" fill="none" stroke="#e31e24" stroke-width="8"/>
  </svg>
  <div class="abs" style="left:128px;top:2504px;width:220px;height:220px;border-radius:50%;background:radial-gradient(circle at 50% 40%,#9a9a9a 0%,#5a5a5a 55%,#2e2e2e 100%)" role="img" aria-label="Portrait of the chief executive officer"></div>
  <div class="abs" style="left:394px;top:2528px;width:1px;height:180px;background:var(--line)"></div>
  <p class="quote">“Lorem ipsum dolor sit amet, consectetur adipiscing elit, sed do eiusmod tempor incididunt ut labore et dolore magna aliqua. Quis ipsum suspendisse ultrices gravida. Risus commodo viverra maecenas Lorem ipsum dolor sit amet, consectetur adipis”</p>
  <div class="quote__name">Daniel Harcourt</div>
  <div class="quote__role">Chief Executive Officer</div>
</section>

<section class="why">
  <svg class="abs" style="left:0;top:0" width="1200" height="640" aria-hidden="true">
    <defs><linearGradient id="whyPhoto" x1="0" y1="0" x2="0" y2="1"><stop offset="0" stop-color="#bdbdbd"/><stop offset=".55" stop-color="#d6d6d6"/><stop offset=".8" stop-color="#7a7a7a"/><stop offset="1" stop-color="#3d3d3d"/></linearGradient></defs>
    <polygon points="754,0 1200,0 1200,640 522,640" fill="url(#whyPhoto)" role="img" aria-label="Modern white apartment building with lawn"/>
    <line x1="719" y1="98" x2="554" y2="532" stroke="#e31e24" stroke-width="4"/>
  </svg>
  <div class="ghost" style="left:155px;top:112px;color:rgba(255,255,255,.07)">WHY US</div>
  <h2 class="h2" style="left:118px;top:150px;color:#fff">WHAT SETS US A PART</h2>
  <div class="rule" style="left:120px;top:201px;width:73px;background:#fff"></div>
  <p class="body-copy" style="left:120px;top:229px;width:440px;color:#fff">Lorem ipsum dolor sit amet, consectetur adipiscing elit, sed do eiusmod tempor incididunt ut labore et dolore</p>
  <p class="body-copy" style="left:120px;top:308px;width:440px;color:#fff">Aagna aliqua. Quis ipsum suspendisse ultrices gravida. Risus commodo viverra maecenas accumsan lacus vel facilisis. Lorem ipsum dolor sit ame</p>
  <a class="btn btn--outline" style="left:120px;top:406px;width:160px;height:45px" href="#">LEARN MORE &rsaquo;</a>
</section>

<footer class="site-footer">
  <div class="brand" style="left:123px;top:3525px;font-size:58px;line-height:66px">VELMORA</div>
  <svg class="abs" style="left:128px;top:3610px" width="140" height="30" aria-hidden="true">
    <circle cx="15" cy="15" r="13" fill="#e31e24"/>
    <circle cx="62" cy="15" r="13" fill="#333"/>
    <rect x="107" y="2" width="26" height="26" fill="#333"/>
  </svg>
  <div class="abs" style="left:394px;top:3532px;width:1px;height:176px;background:var(--line)"></div>

  <svg class="abs" style="left:461px;top:3531px" width="20" height="24" viewBox="0 0 20 24" aria-hidden="true"><path d="M10 1 A8 8 0 0 1 18 9 C18 15 10 23 10 23 C10 23 2 15 2 9 A8 8 0 0 1 10 1Z" fill="#444"/><circle cx="10" cy="9" r="3" fill="#fff"/></svg>
  <div class="footer-contact" style="top:3532px">Maple Grove, NJ</div>
  <div class="abs" style="left:460px;top:3563px;width:228px;height:1px;background:var(--line)"></div>
  <svg class="abs" style="left:460px;top:3580px" width="22" height="22" viewBox="0 0 22 22" aria-hidden="true"><circle cx="11" cy="11" r="10" fill="#444"/><rect x="5.5" y="7" width="11" height="8" fill="none" stroke="#fff" stroke-width="1.2"/><path d="M5.5 7 L11 11.5 L16.5 7" fill="none" stroke="#fff" stroke-width="1.2"/></svg>
  <div class="footer-contact" style="top:3580px">info@velmora.com</div>
  <div class="abs" style="left:460px;top:3614px;width:228px;height:1px;background:var(--line)"></div>
  <div class="footer-label" style="left:461px;top:3629px">CAREER INQUIRIES</div>
  <div class="btn-mail">
    <svg width="15" height="11" viewBox="0 0 15 11" style="vertical-align:-1px;margin-right:5px" aria-hidden="true"><rect x=".6" y=".6" width="13.8" height="9.8" fill="none" stroke="#fff" stroke-width="1.2"/><path d="M.6 .6 L7.5 6 L14.4 .6" fill="none" stroke="#fff" stroke-width="1.2"/></svg>EMAIL US</div>

  <div class="footer-label" style="left:779px;top:3527px">LEAVE MESSAGE</div>
  <div class="field" style="left:779px;top:3562px;width:166px;height:33px">Name</div>
  <div class="field" style="left:953px;top:3562px;width:166px;height:33px">Email</div>
  <div class="field" style="left:779px;top:3603px;width:340px;height:52px">Message</div>
  <div class="btn-send">SEND MESSAGE &rsaquo;</div>

  <div class="copyright">Copyright © 2025 Velmora. All Right Reserved</div>
</footer>

</body>
</html>
```